Your Health, Your Time, Your Way: Personalized, Concierge Care Elevated to Modern Medicine

We need to incorporate an image of our new doctor (Dr. Marlene Quorvath, MD) with our office logo ( Bright Harbor Clinic) and dialogue that shows how simple it is to schedule a free consult and learn what our office has to offer patients. The colors should be consistent with our website- the CMYK codes will be attached for your use below. The font should be easy to read. The text should be clear, and convey value to the patient for chosing us over anyone else ( we offer primary care, preventive medicine, urgen care and functional medicine with 24 hour direct access to care with some of our strengths including focus on individualized care, cutting edge medicine, blended functional and traditional style. We aim to transform lives through patient centered innovative and individualized care plan. I have attached a "mock" image but the details ( office address, name, phone number are incorrect) The correct info is Bright Harbor Clinic 4187 Pellman Ave Suite 214, Clearwater, FL 33798 and phone number (727)555-0148. A possible hook could read: welcoming new patients now- Your Health, Your Time, Your Way: Personalized Care Meets Modern Medicine
Updates

I did not realize that there was a tab with more information to fill for the designers to see, or for me to upload the basic information they need to create the design.

Target Market(s)

Patients over 18 years of age with interest in longevity, functional and traditional medicine; the postcards will be mailed to our CURRENT patients, and they are a reminder of what we do, new patient availability AND a request for them to refer friends or families

Industry/Entity Type

medical

Font styles to use
Sans Serif

Colors

Designer to choose colors to be used in the design.

Requirements
Must have
• simple reminder to current patients of what we offer, and a call to action for our patients to refer friends and family for same level of excellence;consistency with brand ( see business card and cmyx codes for colors);photo of new physician; logo Bright Harbor Clinic, web site (https://brightharborclinic.example); Must clearly express accepting new patients; simple to call/email to schedule free consultation;; include our email (frontdesk@brightharborclinic.example), phone number (727)555-0148; our address 4187 Pellman Ave Suite 214, Clearwater, FL 33798
Nice to have
• photo of our new physician ( in blue jacket: Dr. Marlene Quorvath, MD) should not take up too much space
Should not have
• clutter, or close text; full sentences( bulleted text preferred)

```html
<!DOCTYPE html>
<html lang="en">
<head>
<meta charset="utf-8">
<title>Bright Harbor Clinic – New Doctor Postcard</title>
<link href="https://fonts.googleapis.com/css2?family=Poppins:wght@300;400;500;600;700;800&family=Oswald:wght@400;500;600&display=swap" rel="stylesheet">
<style>
  :root{
    --stage:#8a8a8a;
    --navy:#2f4c70;
    --navy-deep:#263f60;
    --teal:#6cc5cf;
    --teal-band:#5b9db0;
    --teal-mid:#5aa5b5;
    --yellow:#fbf59a;
    --yellow-text:#f6ee6a;
    --red:#c8100c;
    --ink:#4a4a4a;
    --ink-dark:#333;
    --white:#fff;
    --rule:#c4c4c4;
    --stamp:#e6e6e6;
  }
  *{box-sizing:border-box;margin:0;padding:0}
  html,body{width:848px;height:1200px;overflow:hidden}
  body{background:var(--stage);font-family:'Poppins',sans-serif;position:relative}
  .card{position:absolute;left:85px;width:678px;height:452px;overflow:hidden;background:var(--white)}
  .card--front{top:125px;background:linear-gradient(135deg,#fff 0%,#f3f3f3 45%,#fff 100%)}
  .card--back{top:622px}
  .abs{position:absolute}

  /* brand name */
  .brand{display:flex;align-items:center;gap:6px;font-family:'Poppins',sans-serif;font-weight:500;font-size:11px;line-height:1.15;color:#111}
  .brand__dot{width:12px;height:12px;border-radius:50%;background:#111;flex:none}

  /* front */
  .hero-panel{left:40px;top:102px;width:600px;height:207px;border-radius:25px;background:var(--navy)}
  .doctor-photo{left:398px;top:8px;width:242px;height:301px;border-radius:0 0 25px 0;
    background:linear-gradient(180deg,#3a3030 0%,#b9876c 35%,#1d2233 62%,#161b2a 100%)}
  .headline{left:60px;font-weight:500;color:var(--white);font-size:35px;line-height:1}
  .headline--meet{top:121px}
  .headline--new{top:157px}
  .headline--doctor{left:58px;top:186px;font-weight:700;font-size:68px;color:var(--teal);letter-spacing:-1px}
  .hero-rule{left:63px;top:267px;width:47px;height:2px;background:var(--teal)}
  .tagline{left:63px;top:278px;font-weight:600;font-size:15px;color:var(--white)}
  .tagline span{color:var(--yellow-text)}
  .name-tag{left:238px;top:267px;width:182px;height:47px;background:var(--yellow);border-radius:4px;
    display:flex;align-items:center;justify-content:center;white-space:nowrap;
    font-family:'Oswald',sans-serif;font-weight:500;font-size:17px;color:var(--ink-dark);box-shadow:0 2px 3px rgba(0,0,0,.2)}
  .name-tag small{font-weight:400;font-size:17px;margin-left:4px}
  .burst{left:522px;top:256px;width:114px;height:114px}
  .burst__text{left:522px;top:275px;width:114px;text-align:center;color:var(--white);line-height:1.05}
  .burst__text .soft{font-size:13px;font-weight:400;display:block}
  .burst__text .bold{font-size:17px;font-weight:800;display:block}

  .schedule{left:37px;top:327px;font-weight:300;font-size:19px;letter-spacing:5.2px;color:var(--ink)}
  .consult-box{left:38px;top:353px;width:205px;height:30px;background:var(--teal-mid);border-radius:4px;
    font-family:'Oswald',sans-serif;font-weight:500;font-size:23px;line-height:30px;text-align:center;color:var(--white);letter-spacing:.5px}
  .consult-box .free{color:var(--navy)}
  .explore{left:38px;top:387px;width:220px;font-weight:600;font-size:14.5px;line-height:15px;color:#555}
  .divider{left:265px;top:332px;width:1px;height:86px;background:#999}
  .contact-line{left:284px;top:330px;font-weight:700;font-size:11px;color:var(--navy)}
  .contact-line span{color:var(--teal-mid)}
  .phone-big{left:284px;top:342px;display:flex;align-items:center;gap:4px;font-weight:700;font-size:27px;line-height:32px;color:#555;letter-spacing:1px}
  .visit-bar{display:flex;align-items:stretch;overflow:hidden;border-radius:4px}
  .visit-bar--front{left:284px;top:374px;width:355px;height:24px;background:var(--navy)}
  .visit-bar__label{background:var(--teal-mid);color:var(--white);font-weight:600;font-size:12px;display:flex;align-items:center;justify-content:center;flex:none}
  .visit-bar--front .visit-bar__label{width:49px}
  .visit-bar__url{color:var(--white);font-weight:600;font-size:10.5px;display:flex;align-items:center;padding-left:8px;white-space:nowrap}
  .cta-today{left:284px;top:404px;font-size:14px;color:#555;white-space:nowrap}
  .cta-today b{font-weight:700}

  /* back */
  .back-panel{left:0;top:0;width:361px;height:452px;background:var(--navy)}
  .bubble{left:38px;top:37px;width:289px;height:57px;background:var(--yellow);border-radius:5px;padding:8px 9px;box-shadow:0 2px 3px rgba(0,0,0,.2)}
  .bubble__tail{left:52px;top:93px;width:0;height:0;border-left:6px solid transparent;border-right:6px solid transparent;border-top:9px solid var(--yellow)}
  .bubble__title{font-weight:700;font-size:19.5px;line-height:22px;color:var(--navy)}
  .bubble__sub{font-weight:600;font-size:12.5px;line-height:16px;color:#444}
  .bullets{list-style:none;color:var(--white);font-size:8.6px;line-height:10.7px}
  .bullets li{position:absolute;padding-left:10px}
  .bullets li svg{position:absolute;left:0;top:2px}
  .team-photo{left:172px;top:134px;width:185px;height:121px;
    background:linear-gradient(90deg,#b98a72 0%,#e9e6ee 30%,#2a2a2e 55%,#e8e6ee 80%,#c9a183 100%)}
  .band{left:0;top:255px;width:370px;height:68px;background:var(--teal-band)}
  .contact-head{left:38px;top:333px;font-weight:700;font-size:20px;color:var(--teal)}
  .back-phone{top:330px;display:flex;align-items:center;gap:5px;font-weight:700;font-size:18px;color:var(--white)}
  .back-address{top:352px;display:flex;align-items:center;gap:6px;font-size:8.5px;color:var(--white)}
  .visit-bar--back{left:38px;top:371px;width:289px;height:20px;border:1px solid var(--white);border-radius:4px}
  .visit-bar--back .visit-bar__label{width:39px;background:#7bc3cf;font-size:10px}
  .visit-bar--back .visit-bar__url{font-size:9.4px;padding-left:5px}
  .fineprint{left:38px;top:396px;font-size:7.2px;line-height:10px;color:var(--white);white-space:nowrap}
  .fineprint b{color:var(--yellow-text);font-weight:600}
  .stamp{left:575px;top:38px;width:65px;height:70px;background:var(--stamp);border-radius:3px}
  .address-rule{left:384px;width:256px;height:1px;background:var(--rule)}
</style>
</head>
<body>

<!-- FRONT -->
<section class="card card--front">
  <div class="abs brand" style="left:38px;top:44px"><span class="brand__dot"></span>Bright Harbor<br>Clinic</div>

  <div class="abs hero-panel"></div>
  <div class="abs doctor-photo" role="img" aria-label="Portrait photo of Dr. Marlene Quorvath in a navy jacket"></div>

  <div class="abs headline headline--meet">MEET</div>
  <div class="abs headline headline--new">OUR NEW</div>
  <div class="abs headline headline--doctor">Doctor!</div>
  <div class="abs hero-rule"></div>
  <div class="abs tagline">Bright Harbor <span>Clinic</span></div>
  <div class="abs name-tag">MARLENE QUORVATH,<small>MD</small></div>

  <svg class="abs burst" viewBox="0 0 100 100" aria-hidden="true">
    <polygon fill="var(--red)" points="50,0 57,10 69,4 71,17 84,16 80,28 93,33 84,42 96,50 84,58 93,67 80,72 84,84 71,83 69,96 57,90 50,100 43,90 31,96 29,83 16,84 20,72 7,67 16,58 4,50 16,42 7,33 20,28 16,16 29,17 31,4 43,10"/>
  </svg>
  <div class="abs burst__text"><span class="soft">It’s</span><span class="soft">Easy</span><span class="bold">To Get</span><span class="bold">Started!</span></div>

  <div class="abs schedule">SCHEDULE YOUR</div>
  <div class="abs consult-box"><span class="free">FREE</span> CONSULTATION</div>
  <div class="abs explore">And explore the benefits of personalized care</div>
  <div class="abs divider"></div>

  <div class="abs contact-line">CONTACT US <span>FOR MORE INFORMATION</span></div>
  <div class="abs phone-big">
    <svg width="18" height="18" viewBox="0 0 20 20" aria-hidden="true"><circle cx="10" cy="10" r="9" fill="none" stroke="var(--navy)" stroke-width="2"/><path d="M6.5 5.5l2 0 1 2.5-1.2 1a6 6 0 0 0 2.7 2.7l1-1.2 2.5 1v2a1.5 1.5 0 0 1-1.5 1.5A8 8 0 0 1 5 7a1.5 1.5 0 0 1 1.5-1.5z" fill="var(--navy)"/></svg>
    727-555-0148
  </div>
  <div class="abs visit-bar visit-bar--front">
    <span class="visit-bar__label">VISIT</span>
    <span class="visit-bar__url">https://brightharborclinic.example/appointment/</span>
  </div>
  <div class="abs cta-today">TO SCHEDULE YOUR <b>FREE CONSULTATION TODAY</b></div>
</section>

<!-- BACK -->
<section class="card card--back">
  <div class="abs back-panel"></div>

  <div class="abs bubble">
    <div class="bubble__title">BRIGHT HARBOR CLINIC</div>
    <div class="bubble__sub">Welcoming new patients today!</div>
  </div>
  <div class="abs bubble__tail"></div>

  <div class="abs team-photo" role="img" aria-label="Photo of the clinic's three-person care team"></div>

  <ul class="bullets">
    <li style="left:38px;top:116px;white-space:nowrap"><svg width="7" height="7" viewBox="0 0 10 10"><circle cx="5" cy="5" r="5" fill="var(--yellow-text)"/><path d="M2.7 5.2l1.6 1.5 3-3.2" stroke="var(--navy)" stroke-width="1.4" fill="none"/></svg>Concierge Medicine values your goals, time and health.</li>
    <li style="left:38px;top:138px;width:128px"><svg width="7" height="7" viewBox="0 0 10 10"><circle cx="5" cy="5" r="5" fill="var(--yellow-text)"/><path d="M2.7 5.2l1.6 1.5 3-3.2" stroke="var(--navy)" stroke-width="1.4" fill="none"/></svg>At Bright Harbor Clinic, we focus on individualized care and take insurance algorithms out of the equation.</li>
    <li style="left:38px;top:200px;width:128px"><svg width="7" height="7" viewBox="0 0 10 10"><circle cx="5" cy="5" r="5" fill="var(--yellow-text)"/><path d="M2.7 5.2l1.6 1.5 3-3.2" stroke="var(--navy)" stroke-width="1.4" fill="none"/></svg>We use cutting edge technology and tests that make sense for you and your health care goals.</li>
  </ul>

  <div class="abs band"></div>
  <ul class="bullets">
    <li style="left:38px;top:262px;width:150px;padding-left:15px"><svg width="7" height="7" viewBox="0 0 10 10"><circle cx="5" cy="5" r="5" fill="var(--white)"/><path d="M2.7 5.2l1.6 1.5 3-3.2" stroke="var(--teal-band)" stroke-width="1.4" fill="none"/></svg>If you want easy access to your doctor,</li>
    <li style="left:38px;top:291px;width:140px;padding-left:15px"><svg width="7" height="7" viewBox="0 0 10 10"><circle cx="5" cy="5" r="5" fill="var(--white)"/><path d="M2.7 5.2l1.6 1.5 3-3.2" stroke="var(--teal-band)" stroke-width="1.4" fill="none"/></svg>Comfortable one hour or more visits,</li>
    <li style="left:197px;top:262px;width:120px;padding-left:12px"><svg width="7" height="7" viewBox="0 0 10 10"><circle cx="5" cy="5" r="5" fill="var(--white)"/><path d="M2.7 5.2l1.6 1.5 3-3.2" stroke="var(--teal-band)" stroke-width="1.4" fill="none"/></svg>Flexibility of meeting via zoom,</li>
    <li style="left:197px;top:291px;width:140px;padding-left:12px"><svg width="7" height="7" viewBox="0 0 10 10"><circle cx="5" cy="5" r="5" fill="var(--white)"/><path d="M2.7 5.2l1.6 1.5 3-3.2" stroke="var(--teal-band)" stroke-width="1.4" fill="none"/></svg>On phone or in office,</li>
  </ul>

  <div class="abs contact-head">CONTACT US</div>
  <div class="abs back-phone" style="left:188px">
    <svg width="13" height="13" viewBox="0 0 20 20" aria-hidden="true"><circle cx="10" cy="10" r="9" fill="none" stroke="var(--yellow-text)" stroke-width="2"/><path d="M6.5 5.5l2 0 1 2.5-1.2 1a6 6 0 0 0 2.7 2.7l1-1.2 2.5 1v2a1.5 1.5 0 0 1-1.5 1.5A8 8 0 0 1 5 7a1.5 1.5 0 0 1 1.5-1.5z" fill="var(--yellow-text)"/></svg>
    727-555-0148
  </div>
  <div class="abs back-address" style="left:190px">
    <svg width="8" height="10" viewBox="0 0 10 13" aria-hidden="true"><path d="M5 0a4 4 0 0 1 4 4c0 3-4 7-4 7S1 7 1 4a4 4 0 0 1 4-4z" fill="none" stroke="var(--yellow-text)" stroke-width="1.4"/><circle cx="5" cy="4" r="1.3" fill="var(--yellow-text)"/><rect x="1" y="12" width="8" height="1" fill="var(--yellow-text)"/></svg>
    4187 Pellman Ave Suite 214
  </div>
  <div class="abs visit-bar visit-bar--back">
    <span class="visit-bar__label">VISIT</span>
    <span class="visit-bar__url">https://brightharborclinic.example/appointment/</span>
  </div>
  <div class="abs fineprint">Speak to Dana <b>to schedule your free half hour consultation with our doctors.</b><br>You can meet our friendly and knowledgeable team and see our office space.</div>

  <div class="abs brand" style="left:390px;top:58px"><span class="brand__dot"></span>Bright Harbor<br>Clinic</div>
  <div class="abs stamp"></div>
  <div class="abs address-rule" style="top:255px"></div>
  <div class="abs address-rule" style="top:295px"></div>
  <div class="abs address-rule" style="top:334px"></div>
</section>

</body>
</html>
```